The Quiet Ledger Method - Seven Weekend Fixes

Nonfiction book about how to save on insurance. Almost one hundred measures and examples to reduce ones insurance costs.

Target Market(s)

Men/Women between 18 and 50

Industry/Entity Type

Insurance

```html
<!DOCTYPE html>
<html lang="en">
<head>
<meta charset="utf-8">
<title>The Quiet Ledger Method – Cover Spread</title>
<link rel="stylesheet" href="https://fonts.googleapis.com/css2?family=Dosis:wght@500;600;700&family=Noto+Sans:wght@400&display=swap">
<style>
  :root {
    --orange: #f0562a;
    --teal: #1aa596;
    --ink: #3a3a3a;
    --paper: #ffffff;
    --stage: #f1f1f1;
    --muted: #8a8a8a;
    --slot: #c9c9c9;
    --art-top: #f2f2f2;
    --art-bottom: #e2e2e2;
  }
  * { box-sizing: border-box; margin: 0; padding: 0; }
  html, body {
    width: 1200px; height: 711px; overflow: hidden;
    background: var(--stage);
  }
  .spread {
    position: absolute; left: 160px; top: 25px;
    width: 880px; height: 660px;
    background: var(--paper);
    box-shadow: 0 2px 10px rgba(0,0,0,0.12);
    font-family: "Dosis", sans-serif;
  }
  .panel { position: absolute; top: 0; height: 660px; }
  .back  { left: 0; width: 366px; }
  .spine { left: 366px; width: 73px; }
  .front { left: 439px; width: 441px; }

  .title {
    position: absolute; left: 0; right: 0;
    text-transform: uppercase; font-weight: 600; line-height: 1;
  }
  .title .line-a { display: block; color: var(--orange); }
  .title .line-b { display: block; color: var(--teal); }

  .back .title { top: 34px; left: 28px; font-size: 36px; }
  .back .title .line-b { margin-top: 6px; }

  .art {
    position: absolute;
    background: linear-gradient(180deg, var(--art-top), var(--art-bottom));
  }
  .back .art { left: 28px; top: 200px; width: 156px; height: 150px; }

  .blurb {
    position: absolute; left: 218px; top: 190px; width: 138px;
    font-family: "Noto Sans", sans-serif; font-size: 10px; line-height: 1.62;
    color: var(--ink); text-align: justify;
  }
  .back .tagline { position: absolute; left: 30px; top: 398px; font-size: 24px; }

  .tagline { font-weight: 600; text-transform: uppercase; white-space: nowrap; }
  .tagline .o { color: var(--orange); }
  .tagline .t { color: var(--teal); }

  .author-band {
    position: absolute; left: 0; top: 453px; width: 366px; height: 118px;
    background: var(--teal);
  }
  .author-photo {
    position: absolute; left: 32px; top: 15px; width: 66px; height: 84px;
    background: var(--paper);
  }
  .author-bio {
    position: absolute; left: 112px; top: 12px; width: 240px;
    font-family: "Noto Sans", sans-serif; font-size: 10px; line-height: 1.55;
    color: var(--paper); text-align: justify;
  }
  .author-bio strong { font-family: "Dosis", sans-serif; font-weight: 700; font-size: 12px; }

  .publisher {
    position: absolute; left: 32px; top: 606px;
    font-size: 17px; font-weight: 600; color: var(--muted); text-transform: uppercase;
  }
  .isbn-slot {
    position: absolute; left: 258px; top: 592px; width: 72px; height: 50px;
    background: var(--slot);
  }

  .spine-text {
    position: absolute; left: 50%; transform: translateX(-50%);
    writing-mode: vertical-rl;
    color: var(--teal); font-weight: 600; text-transform: uppercase;
    letter-spacing: 3px; white-space: nowrap;
  }
  .spine-title { top: 40px; font-size: 19px; }
  .spine-author { top: 468px; font-size: 24px; font-weight: 700; }

  .front .title { top: 56px; text-align: center; font-size: 48px; }
  .front .title .line-b { margin-top: 8px; }
  .front .art { left: 96px; top: 200px; width: 250px; height: 280px; }
  .front .tagline {
    position: absolute; left: 0; right: 0; top: 518px;
    text-align: center; font-size: 34px;
  }
  .front-band {
    position: absolute; left: 0; top: 578px; width: 441px; height: 82px;
    background: var(--teal);
    display: flex; align-items: center; justify-content: center;
    color: var(--paper); font-size: 40px; font-weight: 700;
    text-transform: uppercase; letter-spacing: 1px;
  }
</style>
</head>
<body>
  <main class="spread">
    <section class="panel back">
      <h2 class="title"><span class="line-a">The Quiet Ledger</span><span class="line-b">Method</span></h2>
      <div class="art" role="img" aria-label="Illustration: umbrella under falling raindrops"></div>
      <p class="blurb">Every policy hides small costs that add up over a year. This book walks through simple checks you can finish on a quiet weekend, from comparing quotes to trimming coverage you no longer need. Each fix comes with a clear example and a short list of steps to follow.</p>
      <p class="tagline"><span class="o">Seven</span> <span class="t">Weekend</span> <span class="o">Fixes</span></p>
      <div class="author-band">
        <div class="author-photo"></div>
        <p class="author-bio"><strong>MARTA VENN</strong> writes about household money in plain words. She has helped hundreds of families cut their premiums without losing the protection they rely on.</p>
      </div>
      <p class="publisher">Publisher's Name</p>
      <div class="isbn-slot"></div>
    </section>

    <section class="panel spine">
      <span class="spine-text spine-title">The Quiet Ledger Method</span>
      <span class="spine-text spine-author">Marta Venn</span>
    </section>

    <section class="panel front">
      <h1 class="title"><span class="line-a">The Quiet Ledger</span><span class="line-b">Method</span></h1>
      <div class="art" role="img" aria-label="Illustration: umbrella under falling raindrops"></div>
      <p class="tagline"><span class="o">Seven</span> <span class="t">Weekend</span> <span class="o">Fixes</span></p>
      <div class="front-band">Marta Venn</div>
    </section>
  </main>
</body>
</html>
```